DORLIT HOMES Professional Home Buyers

Please see two files uploaded. One is my new LOGO (thanks Quenby) and the other gives the wording and pages desired. Of course I am open to suggestions to further enhance what I'm about. I don't want testimonials or houses to buy to appear but to have room for them when I'm ready. I am a real estate investor not a licensed real estate agent. For FAQ i want just the questions to appear and when they click on the question the answer appears and when they click on the question again the answer disappears. make sense? When you read my wording and my idea of pages you'll get an idea of what I'm about. Suggestions are welcomed.

Industry/Entity Type

Real Estate

Number of Pages Required

5+ page

Requirements
Must have
• FAQ pages only questions appear. They click on question the answer appears underneath. they click on question again, the answer disappears. Also, I of course, want my new LOGO to appear on each page I don't know if it will look better all by itself or blended in somehow? Call now 418-555-0193 on each page also. I will get a real phone number before website goes live. If you have a better way of wording what I'm describing please let me know, I am open to feedback
Nice to have
• Anything that the average homeowner can relate to (yea I know, that doesn't help you much, right?)
• Testimonial page and houses to buy page could be done with just the shell ready in the wings for when my business grows it will be ready all that it would need then are the wording and pictures to be uploaded onto the website page. make sense?
Should not have
• I don't want it too elegant or rich looking as I believe my audience will be mostly the average homeowner who needs help

```html
<!DOCTYPE html>
<html lang="en">
<head>
<meta charset="utf-8">
<title>DORLIT HOMES – Professional Home Buyers</title>
<link href="https://fonts.googleapis.com/css2?family=Open+Sans:wght@400;600;700;800&display=swap" rel="stylesheet">
<style>
:root{
  --navy:#1b3668;
  --navy-dark:#132a52;
  --blue:#2d5da8;
  --ink:#333a45;
  --muted:#6b7380;
  --line:#d7dbe2;
  --bg-soft:#eef0f3;
  --white:#ffffff;
  --hero-a:#e9ecef;
  --hero-b:#c9ced5;
}
*{box-sizing:border-box;margin:0;padding:0}
html,body{width:771px;height:1200px;overflow:hidden}
body{font-family:"Open Sans",Arial,sans-serif;color:var(--ink);background:var(--white);font-size:7px;line-height:1.45}
.page{width:771px;height:1200px;position:relative;overflow:hidden}

/* header */
.site-header{height:86px;position:relative;background:var(--white)}
.brand{position:absolute;left:22px;top:12px;display:flex;align-items:center;gap:7px}
.brand-mark{width:22px;height:22px;background:var(--navy)}
.brand-name{font-size:19px;font-weight:800;color:var(--navy);letter-spacing:.5px;line-height:1}
.brand-tag{position:absolute;left:22px;top:40px;font-size:7.5px;font-weight:700;color:var(--navy);letter-spacing:.6px}
.main-nav{position:absolute;right:14px;top:8px;display:flex;gap:4px}
.main-nav a{font-size:7.5px;font-weight:600;color:var(--navy);text-decoration:none;padding:5px 9px;text-transform:uppercase}
.main-nav a.is-active{background:var(--navy);color:var(--white)}
.call-now{position:absolute;right:20px;top:54px;display:flex;align-items:center;gap:6px;font-size:14px;font-weight:800;color:var(--navy)}

/* hero */
.hero{height:182px;position:relative;background:linear-gradient(100deg,var(--hero-a) 0%,#f4f5f6 45%,var(--hero-b) 100%)}
.hero-photo{position:absolute;inset:0}
.hero-copy{position:absolute;left:60px;top:30px;width:260px}
.hero-copy h1{font-size:15px;font-weight:800;color:var(--navy);line-height:1.2}
.hero-copy p{font-size:7px;color:var(--ink);margin-top:4px;width:200px}
.quote-form{position:absolute;right:56px;top:10px;width:150px;height:162px;background:var(--navy);padding:9px 10px}
.quote-form h2{font-size:8.5px;font-weight:700;color:var(--white);text-align:center;margin-bottom:8px}
.quote-form .field{height:17px;background:var(--white);margin-bottom:6px;font-size:6px;color:var(--muted);padding:4px 6px}
.quote-form .submit{margin:4px auto 0;width:72px;height:17px;background:var(--white);color:var(--navy);font-size:7px;font-weight:700;text-align:center;line-height:17px}
.hero-strip{height:14px;background:var(--bg-soft)}

/* cash section */
.cash{height:138px;position:relative}
.cash-image{position:absolute;left:86px;top:20px;width:86px;height:92px;background:linear-gradient(160deg,#f1f2f3,#b9c6d8)}
.cash-copy{position:absolute;left:188px;top:18px;width:500px}
.cash-copy h2{font-size:11px;font-weight:800;color:var(--navy)}
.cash-copy p{font-size:6.5px;margin-top:3px;width:480px}
.cash-copy h3{font-size:6.5px;font-weight:700;margin-top:4px}
.tick-list{list-style:none;display:grid;grid-template-columns:150px 150px;gap:1px 10px;margin-top:3px}
.tick-list li{font-size:6.5px;display:flex;align-items:center;gap:4px}

/* houses */
.houses{height:300px;padding:0 74px}
.houses h2,.faq h2{font-size:11px;font-weight:800;color:var(--navy);margin-bottom:8px}
.house-grid{display:grid;grid-template-columns:1fr 1fr;gap:14px 22px}
.house-card{height:120px;border:1px solid var(--line);padding:8px}
.house-card h3{font-size:7.5px;font-weight:700;color:var(--navy);margin-bottom:5px}
.house-body{display:flex;gap:8px}
.house-photo{width:90px;height:86px;flex:none;background:linear-gradient(170deg,#dbe5ef,#9aa9b8)}
.price{background:var(--navy);color:var(--white);font-size:6px;padding:2px 4px;margin-bottom:3px;font-weight:600}
.house-text{font-size:6px;color:var(--ink)}
.more{display:block;font-size:6px;color:var(--navy);font-weight:700;margin-top:3px}

/* faq */
.faq{height:348px;background:var(--bg-soft);padding:14px 74px}
.faq-item{background:var(--white);border:1px solid var(--line);margin-bottom:8px}
.faq-q{display:flex;justify-content:space-between;align-items:center;height:20px;padding:0 8px;font-size:7px;font-weight:600;color:var(--navy)}
.faq-toggle{width:11px;height:11px;background:var(--muted);color:var(--white);font-size:9px;line-height:11px;text-align:center;font-weight:700}
.faq-a{font-size:6.5px;padding:4px 8px 10px;color:var(--ink)}

/* contact + footer */
.contact-band{height:82px;background:var(--navy);display:flex;align-items:center;justify-content:space-between;padding:0 40px;color:var(--white)}
.contact-band h2{font-size:12px;font-weight:700;letter-spacing:.5px}
.contact-item{display:flex;align-items:center;gap:8px;font-size:11px;font-weight:600}
.contact-icon{width:24px;height:24px;border:1.5px solid var(--white);border-radius:50%;display:flex;align-items:center;justify-content:center}
.site-footer{height:50px;background:var(--navy-dark);display:flex;align-items:center;justify-content:space-between;padding:0 40px}
.footer-nav{display:flex;gap:22px}
.footer-nav a,.copyright{font-size:7px;color:#c8d2e3;text-decoration:none}
</style>
</head>
<body>
<div class="page">

<header class="site-header">
  <div class="brand"><span class="brand-mark"></span><span class="brand-name">DORLIT HOMES</span></div>
  <div class="brand-tag">PROFESSIONAL HOME BUYERS</div>
  <nav class="main-nav">
    <a class="is-active">Home</a><a>About us</a><a>FAQ</a><a>Testimonials</a><a>Houses to buy</a><a>Contact us</a>
  </nav>
  <div class="call-now">
    <svg width="14" height="14" viewBox="0 0 24 24"><path fill="#1b3668" d="M6.6 10.8a15 15 0 0 0 6.6 6.6l2.2-2.2c.3-.3.7-.4 1-.2 1.1.4 2.3.6 3.6.6.6 0 1 .4 1 1V20c0 .6-.4 1-1 1A17 17 0 0 1 3 4c0-.6.4-1 1-1h3.5c.6 0 1 .4 1 1 0 1.3.2 2.5.6 3.6.1.3 0 .7-.2 1z"/></svg>
    CALL NOW! 418-555-0193
  </div>
</header>

<section class="hero">
  <div class="hero-photo" role="img" aria-label="Hands signing papers beside a small model house"></div>
  <div class="hero-copy">
    <h1>WE BUY HOUSES IN ANY CONDITION!</h1>
    <p>Don't settle for less when selling your home. DORLIT HOMES is a trusted local home buyer across Maryland.</p>
  </div>
  <form class="quote-form">
    <h2>GET YOUR FREE QUOTE</h2>
    <div class="field">Enter Your Name</div>
    <div class="field">Enter Your Phone No.</div>
    <div class="field">Enter Your City</div>
    <div class="field">Select Your State</div>
    <div class="submit">GET QUOTE</div>
  </form>
</section>
<div class="hero-strip"></div>

<section class="cash">
  <div class="cash-image" role="img" aria-label="Model house with keys and cash"></div>
  <div class="cash-copy">
    <h2>GET CASH FOR YOUR HOUSE!</h2>
    <p>DORLIT HOMES buys houses fast for a fair cash price. No repairs, no cleaning, no agent fees and no waiting on bank approvals. We close on the date you choose.</p>
    <h3>Sell your house FAST!</h3>
    <ul class="tick-list">
      <li>✓ We pay all costs</li><li>✓ We pay with cash quickly</li>
      <li>✓ We buy "as is"</li><li>✓ No waiting for bank approvals</li>
      <li>✓ Quick closings</li><li>✓ No commissions at all</li>
    </ul>
  </div>
</section>

<section class="houses">
  <h2>HOUSES TO BUY</h2>
  <div class="house-grid">
    <article class="house-card">
      <h3>Lorem Ipsum is simply dummy text</h3>
      <div class="house-body">
        <div class="house-photo" role="img" aria-label="Single family home exterior"></div>
        <div><div class="price">$185,000 - Single Family Home</div>
        <p class="house-text">Three bedrooms, two baths, a large fenced yard and a new roof. Close to schools, parks and shopping.</p>
        <a class="more">» More Details</a></div>
      </div>
    </article>
    <article class="house-card">
      <h3>Lorem Ipsum is simply dummy text</h3>
      <div class="house-body">
        <div class="house-photo" role="img" aria-label="Two storey family home exterior"></div>
        <div><div class="price">$210,000 - Single Family Home</div>
        <p class="house-text">Four bedrooms on a quiet street with a two car garage, updated kitchen and finished basement.</p>
        <a class="more">» More Details</a></div>
      </div>
    </article>
    <article class="house-card">
      <h3>Lorem Ipsum is simply dummy text</h3>
      <div class="house-body">
        <div class="house-photo" role="img" aria-label="Brick home with front porch"></div>
        <div><div class="price">$164,000 - Single Family Home</div>
        <p class="house-text">Cozy brick home with a covered porch, hardwood floors and a sunny backyard for the family.</p>
        <a class="more">» More Details</a></div>
      </div>
    </article>
    <article class="house-card">
      <h3>Lorem Ipsum is simply dummy text</h3>
      <div class="house-body">
        <div class="house-photo" role="img" aria-label="Modern home with lawn"></div>
        <div><div class="price">$235,000 - Single Family Home</div>
        <p class="house-text">Bright open floor plan, three bedrooms, large deck and a wide lawn near the town center.</p>
        <a class="more">» More Details</a></div>
      </div>
    </article>
  </div>
</section>

<section class="faq">
  <h2>FAQ</h2>
  <div class="faq-item"><div class="faq-q">What kind of houses do you buy?<span class="faq-toggle">+</span></div></div>
  <div class="faq-item">
    <div class="faq-q">Where do you buy properties?<span class="faq-toggle">−</span></div>
    <p class="faq-a">We buy houses all over Maryland, in cities, suburbs and small towns. Whether your home is in great shape or needs major repairs, we will look at it and make you a fair cash offer. Call us or fill in the form to get started today.</p>
  </div>
  <div class="faq-item"><div class="faq-q">Do you buy higher priced properties?<span class="faq-toggle">+</span></div></div>
  <div class="faq-item"><div class="faq-q">What if I am behind on payments or in foreclosure can you help?<span class="faq-toggle">+</span></div></div>
  <div class="faq-item"><div class="faq-q">What do you charge for your services?<span class="faq-toggle">+</span></div></div>
</section>

<section class="contact-band">
  <h2>CONTACT US</h2>
  <div class="contact-item"><span class="contact-icon"><svg width="12" height="12" viewBox="0 0 24 24"><path fill="#fff" d="M6.6 10.8a15 15 0 0 0 6.6 6.6l2.2-2.2c.3-.3.7-.4 1-.2 1.1.4 2.3.6 3.6.6.6 0 1 .4 1 1V20c0 .6-.4 1-1 1A17 17 0 0 1 3 4c0-.6.4-1 1-1h3.5c.6 0 1 .4 1 1 0 1.3.2 2.5.6 3.6.1.3 0 .7-.2 1z"/></svg></span>418-555-0193</div>
  <div class="contact-item"><span class="contact-icon"><svg width="12" height="12" viewBox="0 0 24 24"><path fill="none" stroke="#fff" stroke-width="2" d="M3 6h18v12H3zM3 6l9 7 9-7"/></svg></span>info@dorlithomes.com</div>
  <div class="contact-item"><span class="contact-icon"><svg width="12" height="12" viewBox="0 0 24 24"><path fill="#fff" d="M12 2a7 7 0 0 0-7 7c0 5 7 13 7 13s7-8 7-13a7 7 0 0 0-7-7zm0 9.5A2.5 2.5 0 1 1 12 6.5a2.5 2.5 0 0 1 0 5z"/></svg></span>14 Harlow Court, Maryland</div>
</section>

<footer class="site-footer">
  <nav class="footer-nav"><a>Home</a><a>About us</a><a>FAQ</a><a>Testimonials</a><a>Houses to buy</a><a>Contact us</a></nav>
  <p class="copyright">Copyright © 2015 Dorlit Homes. All Rights Reserved</p>
</footer>

</div>
</body>
</html>
```